依頼詳細
ポスティングを行いますので、そのためのチラシを作製頂きたいと思います。

①一見して業態が伝わるようなデザインにして頂けるとありがたいです。文字だけでなく、イラスト等も入れてキャッチ―な感じにして下さい。

②1回限り、10km圏内の出張費を無料にするという内容のチケットを組み込んで下さい。

③使用して頂きたい文言の例は以下の通りです。(あくまでも例ですので、適宜変更・追加して頂いても問題ございません。)
・パソコンのことなら何でもご相談下さい
・診断やお見積もりは無料です
・自社内修理なので迅速対応
・ご予算や用途に合わせたBTO PCも販売

④相談してもらいたい困り事の例は以下の通りです。(必ずしも全て入れて頂く必要はありません。)
・パソコンの動作が遅い
・突然起動しなくなった
・ネットに繋がらない
・設定方法がわからない
・操作方法を教えて欲しい
・ウイルスに感染したかもしれない
・突然電源が落ちたりフリーズする
・画面が映らない
・黒い画面に英語のメッセージが表示される

記載項目
屋号:PC NEXLO(ピーシーネクスロ)
住所:気仙沼市北瀬32-4 モルタナとなり
電話・FAX共通:0226-48-3071
営業時間:10時~21時 年中無休
メール:pcnexlo@vqt-net.com
Web:www.vqt-net.com
支払い:クレジットカード利用可
その他:所在地略図
サイズ
B4
ページ数
片面
希望イメージ
シンプル 複雑
単色 カラフル
暗い 明るい
日常 高級
遊び心 厳粛
未来的 伝統的
女性的 男性的
希望する色
青系
納品ファイル
• イラストレーター形式 (.ai)
補足説明
作製に当たって不足している情報等がありましたら、メッセージにてご連絡を頂けましたら幸いです。
多数の皆様から様々なご提案を頂き、誠にありがとうございました。改めて御礼
申し上げます。

力作揃いで非常に悩ましいところではございますが、出来るだけ早く最終的な選定
を行わせて頂きたいと存じます。

本来であれば、お一方ずつ御礼を述べさせて頂きたいところではございますが、とり
急ぎ本欄より失礼致します。引き続き宜しくお願い申し上げます。
■ 選んだ理由

ご提案頂いた際、サムネイル画像を見ただけでもインパクトがあり、訴求したい要件も非常にうまくまとめられておりました。当方では気付かないような細かい点までご配慮頂くなど、要望以上のご提案を頂くことが出来ました。改めて御礼申し上げます。

■ 提案者全員のお礼・コメント

この度は多くのランサー様から多数の力作をご提案頂き、本当にありがとうございました。何れの作品も素晴らしく、選定も非常に難航致しました。今後も定期的に案件をお願いする機会があると思いますので、その際もご提案賜れましたら幸いです。今後とも宜しくお願い申し上げます。

```html
<!DOCTYPE html>
<html lang="ja">
<head>
<meta charset="utf-8">
<title>PC NEXLO チラシ</title>
<link rel="stylesheet" href="https://fonts.googleapis.com/css2?family=Noto+Sans+JP:wght@400;500;700;900&family=Roboto:wght@700;900&display=swap">
<style>
:root{
  --blue:#1479c9;
  --blue-dark:#0e5fa8;
  --red:#e5322a;
  --ink:#1a1a1a;
  --yellow:#f7d21a;
  --white:#ffffff;
}
*{margin:0;padding:0;box-sizing:border-box}
html,body{width:848px;height:1200px;overflow:hidden;background:var(--white)}
body{font-family:"Noto Sans JP",sans-serif;color:var(--ink)}
.flyer{position:relative;width:848px;height:1200px;overflow:hidden;background:var(--white)}
.photo{position:absolute;left:0;top:395px;width:848px;height:573px;background:linear-gradient(160deg,#ffffff 0%,#eceae8 45%,#d9d4cf 100%)}
.headline{position:absolute;left:0;right:0;top:4px;text-align:center;font-weight:500;line-height:1.06;letter-spacing:1px}
.headline .line{display:block;font-size:128px;white-space:nowrap}
.headline .accent-red{color:var(--red)}
.headline .accent-blue{color:var(--blue)}
.points{position:absolute;left:38px;top:300px;list-style:none;font-size:22px;font-weight:700;line-height:1.35}
.points li{display:flex;align-items:center;margin-bottom:2px;white-space:nowrap}
.points li::before{content:"";width:17px;height:17px;border-radius:50%;background:var(--blue);margin-right:7px}
.coupon-string{position:absolute;left:745px;top:175px}
.coupon{position:absolute;left:588px;top:262px;width:236px;height:100px;transform:rotate(-4deg)}
.coupon-card{position:absolute;left:0;top:0;width:236px;height:72px;background:var(--yellow);border-radius:5px;color:var(--white);padding:0 12px}
.coupon .once{position:absolute;right:10px;top:-20px;font-size:14px;font-weight:700;color:var(--ink)}
.coupon .title{font-size:32px;font-weight:900;line-height:72px;white-space:nowrap;letter-spacing:0}
.coupon .note{position:absolute;left:4px;top:76px;font-size:13px;font-weight:700;color:var(--ink);white-space:nowrap}
.connectors{position:absolute;left:0;top:330px}
.trouble{position:absolute;border-radius:50%;background:var(--red);color:var(--white);display:flex;align-items:center;justify-content:center;text-align:center;font-weight:700;font-size:19px;line-height:1.3;box-shadow:0 3px 8px rgba(0,0,0,.18);white-space:nowrap}
.card-ok{position:absolute;left:742px;top:880px;width:96px;height:96px;border-radius:50%;background:var(--blue);color:var(--white);font-size:13px;font-weight:700;display:flex;align-items:flex-end;justify-content:center;padding-bottom:16px;text-align:center;line-height:1.2}
.card-ok::before{content:"";position:absolute;left:30px;top:22px;width:36px;height:26px;border-radius:4px;background:var(--white)}
.contact-label{position:absolute;left:24px;top:942px;background:var(--red);color:var(--white);font-size:16px;font-weight:700;padding:2px 14px;border-radius:4px 4px 0 0}
.contact{position:absolute;left:0;top:968px;width:848px;height:232px;background:var(--blue);color:var(--white)}
.contact .lead{position:absolute;left:22px;top:6px;font-size:19px;font-weight:700}
.contact .phone{position:absolute;left:22px;top:30px;display:flex;align-items:center;font-family:"Roboto",sans-serif;font-weight:900;font-size:58px;letter-spacing:1px}
.contact .phone .tag{font-family:"Noto Sans JP",sans-serif;font-size:13px;font-weight:700;position:absolute;right:-6px;bottom:-8px}
.contact .mail{position:absolute;left:22px;top:104px;display:flex;align-items:center;font-family:"Roboto",sans-serif;font-weight:700;font-size:40px}
.icon{width:52px;height:52px;border-radius:50%;background:var(--white);display:flex;align-items:center;justify-content:center;margin-right:10px;flex:none}
.mail .icon{width:44px;height:44px}
.map{position:absolute;left:560px;top:30px;width:268px;height:124px;background:var(--white);border-radius:6px;color:var(--blue-dark);font-size:38px;font-weight:700;display:flex;align-items:center;justify-content:center}
.footer{position:absolute;left:0;bottom:0;width:848px;height:62px;background:var(--blue-dark);display:flex;align-items:center;padding:0 22px}
.brand{display:flex;flex-direction:column;font-weight:700}
.brand .tagline{font-size:12px}
.brand .name{font-size:30px;letter-spacing:1px;line-height:1}
.info{margin-left:auto;font-size:13px;line-height:1.45;font-weight:500;text-align:left}
</style>
</head>
<body>
<main class="flyer">
  <div class="photo" role="img" aria-label="ノートパソコンを手に困った表情を見せる男性の写真"></div>

  <h1 class="headline">
    <span class="line">その<span class="accent-red">困</span>った!</span>
    <span class="line"><span class="accent-blue">解決</span>します</span>
  </h1>

  <ul class="points">
    <li>自社内修理なので迅速対応</li>
    <li>ご予算や用途に合わせたBTO PCも販売</li>
  </ul>

  <svg class="coupon-string" width="30" height="90" viewBox="0 0 30 90"><path d="M15 0 C5 30 25 55 12 90" fill="none" stroke="#c9a400" stroke-width="2"/></svg>
  <div class="coupon">
    <div class="coupon-card">
      <span class="once">1回限り</span>
      <div class="title">無料クーポン</div>
    </div>
    <div class="note">10km圏内の出張費を無料</div>
  </div>

  <svg class="connectors" width="848" height="640" viewBox="0 0 848 640">
    <g fill="none" stroke="var(--red)" stroke-width="2" stroke-dasharray="5 5">
      <path d="M320 185 L420 260"/>
      <path d="M440 220 L445 280"/>
      <path d="M283 255 L400 280"/>
      <path d="M320 360 L410 310"/>
      <path d="M367 450 L420 330"/>
    </g>
  </svg>

  <div class="trouble" style="left:220px;top:420px;width:120px;height:120px">突然起動<br>しなくなった</div>
  <div class="trouble" style="left:370px;top:410px;width:140px;height:140px">パソコンの<br>動作が遅い</div>
  <div class="trouble" style="left:185px;top:530px;width:100px;height:100px">ネットに<br>繋がらない</div>
  <div class="trouble" style="left:198px;top:650px;width:127px;height:127px">操作方法を<br>教えて欲しい</div>
  <div class="trouble" style="left:325px;top:780px;width:86px;height:86px">...etc</div>

  <div class="card-ok">クレジット<br>カードOK!</div>

  <div class="contact-label">お問合せは</div>
  <section class="contact">
    <p class="lead">診断・お見積は無料です！お気軽にお問合せ下さい！</p>
    <div class="phone">
      <span class="icon"><svg width="28" height="28" viewBox="0 0 24 24"><path fill="#1479c9" d="M6.6 10.8a15.1 15.1 0 0 0 6.6 6.6l2.2-2.2c.3-.3.7-.4 1-.2 1.1.4 2.3.6 3.6.6.6 0 1 .4 1 1V20c0 .6-.4 1-1 1A17 17 0 0 1 3 4c0-.6.4-1 1-1h3.5c.6 0 1 .4 1 1 0 1.3.2 2.5.6 3.6.1.3 0 .7-.2 1z"/></svg></span>
      0226-48-3071
      <span class="tag">TEL&amp;FAX 兼用</span>
    </div>
    <div class="mail">
      <span class="icon"><svg width="24" height="24" viewBox="0 0 24 24"><path fill="#1479c9" d="M3 5h18c.6 0 1 .4 1 1v12c0 .6-.4 1-1 1H3c-.6 0-1-.4-1-1V6c0-.6.4-1 1-1zm9 7.5L20.5 7h-17z"/></svg></span>
      pcnexlo@vqt-net.com
    </div>
    <div class="map">Map</div>
    <footer class="footer">
      <div class="brand">
        <span class="tagline">PCの困ったを解決！</span>
        <span class="name">PC NEXLO</span>
      </div>
      <div class="info">
        営業時間：10時～21時 年中無休<br>
        気仙沼市北瀬32-4 モルタナとなり　www.vqt-net.com
      </div>
    </footer>
  </section>
</main>
</body>
</html>
```